Design business cards for Ironvale Barbers (Opening March so won't need finalised till January2018

Ironvale Barbers is the new age barbers and skincare for all men. Creating tailor made haircuts & customised skincare solutions for the perfect healthy manly look. The Barbers will have a industrial, rustic, worldly feel about it. Rustic red brick wall with old wine barrels as the work stations with the old fashion barber chairs. Concrete floor and a bit corrugated iron around.
Target Market(s)
Professional males who like a great haircut, wet shave and may consider a facial if in the right environment. Total pampering experience in a boys environment.
Industry/Entity Type
Barber
Contact Information for Business Card
Front- Logo - address is 42 Kowhai Rd Taupo
Ph - (07) 348 6192
www.ironvalebarbers.com
email - hello@ironvale.co.nz
Back of card
Mens Haircare - Wet Shaving - Facials - Skin Prescriptions
We are doing a loyalty program - 6 squares numbered then 7th free
Colors
Designer to choose colors to be used in the design.
Requirements
Must have
- Clean simple easy to read.
Nice to have
- Our current colours are white font on black background but thinking we need to introduce another colour. Maybe white logo on a copper, bronze or rusty background. Or even a rustic red brick wall with white writing. Want it clean simple to read. Maybe a burgundy?
Should not have
- no images like heads, scissors, razors please

```html
<!DOCTYPE html>
<html lang="en">
<head>
<meta charset="utf-8">
<title>Ironvale Barbers – Business Card</title>
<link rel="stylesheet" href="https://fonts.googleapis.com/css2?family=Oswald:wght@400;500;600;700&family=Poiret+One&family=Alfa+Slab+One&display=swap">
<style>
  :root {
    --ink: #3a1f22;
    --brick: #87503f;
    --brick-deep: #6f3f33;
    --paper: #f4f0ec;
    --white: #ffffff;
    --tint: #d9cfc5;
    --box-line: #6b4a4c;
  }
  * { box-sizing: border-box; margin: 0; padding: 0; }
  html, body { width: 1072px; height: 1200px; overflow: hidden; background: var(--white); }
  body { position: relative; font-family: "Oswald", sans-serif; color: var(--paper); }

  .card { position: absolute; left: 152px; width: 768px; height: 487px; overflow: hidden; }
  .card--front { top: 89px; }
  .card--back { top: 614px; height: 489px; }

  .brick-wall {
    position: absolute; inset: 0;
    background: linear-gradient(160deg, var(--brick) 0%, var(--brick-deep) 100%);
  }

  /* Front */
  .brand { position: absolute; left: 0; right: 0; top: 24px; text-align: center; color: var(--paper); }
  .brand__name {
    display: block; font-family: "Oswald", sans-serif; font-weight: 600;
    font-size: 118px; line-height: 1; letter-spacing: 2px; text-transform: uppercase;
  }
  .brand__trade {
    display: block; font-family: "Oswald", sans-serif; font-weight: 600;
    font-size: 36px; line-height: 1; letter-spacing: 12px; text-transform: uppercase; margin-top: 10px;
  }

  .contact-panel {
    position: absolute; left: 0; top: 246px; width: 558px; height: 241px;
    background: var(--ink); box-shadow: 6px 6px 10px rgba(0,0,0,0.45);
  }
  .contact-panel__phone {
    position: absolute; left: 43px; top: 28px; font-weight: 500; font-size: 52px;
    line-height: 1; letter-spacing: 7px; white-space: nowrap;
  }
  .contact-panel__phone-icon { position: absolute; left: 433px; top: 35px; width: 64px; height: 44px; }
  .contact-panel__rule { position: absolute; left: 31px; top: 98px; width: 466px; border-top: 2px dashed var(--paper); }
  .contact-panel__rule::after { content: ""; position: absolute; left: 0; right: 0; top: 3px; border-top: 1px solid var(--paper); }
  .contact-panel__address {
    position: absolute; left: 31px; top: 113px; font-weight: 500; font-size: 46px;
    line-height: 1; letter-spacing: 1px; white-space: nowrap; text-transform: uppercase;
  }
  .contact-panel__email, .contact-panel__web {
    position: absolute; top: 184px; font-size: 19px; line-height: 1; white-space: nowrap; text-transform: uppercase;
  }
  .contact-panel__email { left: 35px; font-weight: 500; }
  .contact-panel__web { left: 263px; font-weight: 400; letter-spacing: 0.3px; }

  .social-tile {
    position: absolute; left: 553px; width: 88px; height: 88px;
    background: var(--white); box-shadow: 4px 4px 8px rgba(0,0,0,0.35);
  }
  .social-tile--first { top: 259px; }
  .social-tile--second { top: 363px; }

  /* Back */
  .loyalty-panel {
    position: absolute; left: 510px; top: 51px; width: 232px; height: 387px; background: var(--white);
  }
  .loyalty-panel__stamp {
    position: absolute; width: 67px; height: 67px; border: 2px solid var(--box-line);
    color: var(--tint); font-weight: 500; font-size: 40px; line-height: 63px; text-align: center;
  }
  .loyalty-panel__reward {
    position: absolute; left: 65px; top: 337px; width: 156px; height: 64px;
    background: var(--ink); color: var(--paper); font-weight: 600; font-size: 40px;
    line-height: 64px; text-align: center; white-space: nowrap; letter-spacing: 1px;
  }
  .loyalty-panel__reward sup { font-size: 18px; vertical-align: 16px; text-decoration: underline; }

  .services-panel {
    position: absolute; left: 0; top: 0; width: 553px; height: 436px;
    background: var(--ink); box-shadow: 6px 6px 12px rgba(0,0,0,0.5);
  }
  .services-panel__item { position: absolute; left: 0; width: 100%; text-align: center; white-space: nowrap; line-height: 1; }
  .services-panel__item--haircare {
    top: 48px; font-family: "Alfa Slab One", serif; font-size: 40px; letter-spacing: 2px;
  }
  .services-panel__item--shaving {
    top: 136px; font-family: "Poiret One", sans-serif; font-weight: 400; font-size: 74px; letter-spacing: 0;
  }
  .services-panel__item--facials {
    top: 218px; font-family: "Alfa Slab One", serif; font-size: 84px; letter-spacing: 5px;
  }
  .services-panel__item--skin {
    top: 340px; font-family: "Oswald", sans-serif; font-weight: 400; font-size: 46px; letter-spacing: 0.5px;
  }
  .services-panel__dash { position: absolute; left: 38px; width: 462px; border-top: 2px dashed var(--paper); }
  .services-panel__line { position: absolute; left: 38px; width: 462px; border-top: 1px solid var(--paper); }
  .services-panel__zigzag { position: absolute; left: 38px; top: 318px; width: 462px; height: 10px; }
</style>
</head>
<body>

<section class="card card--front" aria-label="Business card front">
  <div class="brick-wall" role="img" aria-label="Red brick wall texture"></div>

  <h1 class="brand">
    <span class="brand__name">Ironvale</span>
    <span class="brand__trade">Barbers</span>
  </h1>

  <div class="contact-panel">
    <p class="contact-panel__phone">(07) 348 6192</p>
    <svg class="contact-panel__phone-icon" viewBox="0 0 64 44" aria-hidden="true">
      <path d="M4 14 C4 4 60 4 60 14 L60 18 L46 18 L46 12 L18 12 L18 18 L4 18 Z" fill="#f4f0ec"/>
      <path d="M16 20 L48 20 L56 42 L8 42 Z" fill="#f4f0ec"/>
      <g fill="#3a1f22">
        <rect x="24" y="25" width="4" height="3"/><rect x="30" y="25" width="4" height="3"/><rect x="36" y="25" width="4" height="3"/>
        <rect x="24" y="30" width="4" height="3"/><rect x="30" y="30" width="4" height="3"/><rect x="36" y="30" width="4" height="3"/>
        <rect x="24" y="35" width="4" height="3"/><rect x="30" y="35" width="4" height="3"/><rect x="36" y="35" width="4" height="3"/>
      </g>
    </svg>
    <div class="contact-panel__rule"></div>
    <p class="contact-panel__address">42 Kowhai Rd Taupo</p>
    <p class="contact-panel__email">hello@ironvale.co.nz</p>
    <p class="contact-panel__web">www.ironvalebarbers.com</p>
  </div>

  <div class="social-tile social-tile--first" aria-hidden="true"></div>
  <div class="social-tile social-tile--second" aria-hidden="true"></div>
</section>

<section class="card card--back" aria-label="Business card back">
  <div class="brick-wall" role="img" aria-label="Red brick wall texture"></div>

  <div class="loyalty-panel">
    <span class="loyalty-panel__stamp" style="left:65px;top:34px">1</span>
    <span class="loyalty-panel__stamp" style="left:150px;top:34px">2</span>
    <span class="loyalty-panel__stamp" style="left:65px;top:118px">3</span>
    <span class="loyalty-panel__stamp" style="left:150px;top:118px">4</span>
    <span class="loyalty-panel__stamp" style="left:65px;top:202px">5</span>
    <span class="loyalty-panel__stamp" style="left:150px;top:202px">6</span>
    <p class="loyalty-panel__reward">7<sup>TH</sup> FREE</p>
  </div>

  <div class="services-panel">
    <div class="services-panel__dash" style="top:52px"></div>
    <p class="services-panel__item services-panel__item--haircare">MENS HAIRCARE</p>
    <div class="services-panel__line" style="top:104px"></div>
    <div class="services-panel__dash" style="top:110px"></div>
    <p class="services-panel__item services-panel__item--shaving">WET SHAVING</p>
    <p class="services-panel__item services-panel__item--facials">FACIALS</p>
    <svg class="services-panel__zigzag" viewBox="0 0 462 10" preserveAspectRatio="none" aria-hidden="true">
      <line x1="0" y1="2" x2="462" y2="2" stroke="#f4f0ec" stroke-width="1"/>
      <polyline fill="none" stroke="#f4f0ec" stroke-width="1"
        points="0,9 6,4 12,9 18,4 24,9 30,4 36,9 42,4 48,9 54,4 60,9 66,4 72,9 78,4 84,9 90,4 96,9 102,4 108,9 114,4 120,9 126,4 132,9 138,4 144,9 150,4 156,9 162,4 168,9 174,4 180,9 186,4 192,9 198,4 204,9 210,4 216,9 222,4 228,9 234,4 240,9 246,4 252,9 258,4 264,9 270,4 276,9 282,4 288,9 294,4 300,9 306,4 312,9 318,4 324,9 330,4 336,9 342,4 348,9 354,4 360,9 366,4 372,9 378,4 384,9 390,4 396,9 402,4 408,9 414,4 420,9 426,4 432,9 438,4 444,9 450,4 456,9 462,4"/>
    </svg>
    <p class="services-panel__item services-panel__item--skin">SKIN PRESCRIPTIONS</p>
  </div>
</section>

</body>
</html>
```